Real estate sales brochure-Brisquelta

It need to be a real estate sales brochure. A template how I can always adapt the object. In the appendix a sample, please different structure and different design.

Target Market(s)

beautiful presentation of the properties for sale, a Word template

Industry/Entity Type

Real estate

Font styles to use
Serif
Sans Serif

Colors

Designer to choose colors to be used in the design.

Requirements
Must have
• DIN A4 format, Picture not all but some https://files.parvenko.net/share/folders/84kRtWq2mZ9xLpVbNc3dHy-7gTsuAebYoK?view=open
Nice to have
• Color: R187, G214, B: 49 or R119, G187, B66, space for picutre and text

```html
<!DOCTYPE html>
<html lang="de">
<head>
<meta charset="utf-8">
<title>Brisquelta – Verkaufsbroschüre</title>
<link href="https://fonts.googleapis.com/css2?family=Open+Sans:wght@400;700&family=Roboto+Condensed:wght@300;400;700&family=Raleway:wght@400;500&family=Montserrat:wght@400;600&display=swap" rel="stylesheet">
<style>
:root{
  --lime:#bbd631;
  --green:#5cb245;
  --photo-green:#4f9e34;
  --text:#6b6b6b;
  --dark:#4a4a4a;
  --faint:#eeeeee;
  --band:#f0f0f0;
  --stage:#2d2d2d;
  --white:#ffffff;
}
*{margin:0;padding:0;box-sizing:border-box}
html,body{width:1200px;height:1087px;overflow:hidden;background:var(--stage)}
.page{position:absolute;width:283px;height:396px;background:var(--white);overflow:hidden;box-shadow:0 4px 10px rgba(0,0,0,.45);font-family:'Raleway',sans-serif;color:var(--text)}
.p1{left:107px;top:105px}.p2{left:455px;top:105px}.p3{left:811px;top:105px}
.p4{left:107px;top:583px}.p5{left:455px;top:583px}.p6{left:811px;top:585px}
.abs{position:absolute}
.shapes{position:absolute;left:0;top:0}
.brand{font-family:'Open Sans',sans-serif;font-weight:700;white-space:nowrap}
.brand-faint{color:var(--faint);font-size:30px}
.footer-url{position:absolute;left:29px;top:377px;font-family:'Montserrat',sans-serif;font-size:4.6px;letter-spacing:2.6px;color:var(--lime)}
.footer-brand{position:absolute;right:10px;top:370px;font-size:12px;color:var(--lime)}
.rule{position:absolute;height:1.5px;background:var(--lime)}
.rule::before{content:"";position:absolute;left:-2px;top:-2px;width:5px;height:5px;border-radius:50%;background:var(--lime)}
.rule.center::before{left:50%;margin-left:-2.5px}
.cover-title{position:absolute;font-family:'Roboto Condensed',sans-serif;font-weight:300;color:var(--text);font-size:21px;white-space:nowrap}
.for-sale{position:absolute;left:100px;top:312px;font-family:'Roboto Condensed',sans-serif;font-weight:700;font-style:italic;font-size:31px;letter-spacing:2px;color:var(--lime);word-spacing:6px}
.frame{position:absolute;border:1px solid #d8d8d8;background:var(--white);padding:4px}
.features{position:absolute;left:22px;top:224px;list-style:none}
.features li{font-family:'Montserrat',sans-serif;font-size:7px;letter-spacing:.7px;color:var(--dark);height:31px;position:relative;padding-left:11px}
.features li::before{content:"";position:absolute;left:0;top:3px;width:2px;height:2px;border-radius:50%;background:var(--dark)}
.features b{font-weight:600}
.section-title{position:absolute;font-family:'Roboto Condensed',sans-serif;font-weight:700;color:var(--green);white-space:nowrap}
.body-copy{font-size:4.4px;line-height:10.8px;text-align:justify}
.body-copy p{margin-bottom:11px}
.label{position:absolute;font-size:6px;font-weight:500;color:var(--lime)}
.col-text{position:absolute;left:115px;width:121px;font-size:3.9px;line-height:7.1px;text-align:justify}
.col-text p{margin-bottom:7px}
.hyp-title{position:absolute;left:139px;top:110px;font-family:'Open Sans',sans-serif;font-size:10px;font-weight:700;color:var(--lime)}
.hyp-text{position:absolute;left:139px;top:125px;width:110px;font-size:4.5px;line-height:11.6px;text-align:justify}
.hyp-text p{margin-bottom:11px}
.cond-title{position:absolute;left:32px;top:246px;font-family:'Open Sans',sans-serif;font-size:14px;font-weight:700;color:var(--green)}
.cond-row{position:absolute;left:32px;width:234px;font-size:5.4px;line-height:6.5px}
.cond-row .key{position:absolute;left:0;color:var(--lime);font-weight:500}
.cond-row .val{position:absolute;left:66px;width:168px;color:var(--dark)}
.contact{position:absolute;left:137px;top:311px;border-left:1px solid var(--lime);padding-left:4px;height:64px}
.contact .name{font-family:'Raleway',sans-serif;font-size:12px;color:var(--lime);line-height:13px}
.contact .role{font-size:7px;color:var(--dark);margin-bottom:5px}
.contact .line{font-size:6.8px;color:var(--dark);line-height:11px;display:flex;align-items:center;gap:3px;white-space:nowrap}
.contact .dot{width:5px;height:5px;border-radius:50%;background:var(--lime);flex:none}
</style>
</head>
<body>

<!-- Cover -->
<section class="page p1">
  <svg class="shapes" width="283" height="396" viewBox="0 0 283 396">
    <defs>
      <linearGradient id="houseTone" x1="0" y1="0" x2="1" y2="1">
        <stop offset="0" stop-color="#5fae3c"/><stop offset="1" stop-color="#3f8a2a"/>
      </linearGradient>
    </defs>
    <polygon points="0,0 262,0 98,205 0,110" fill="url(#houseTone)" role="img" aria-label="Photo of the house facade in green tint"/>
    <polygon points="262,0 283,0 283,12 98,223 0,150 0,110 98,205" fill="var(--lime)"/>
    <circle cx="198" cy="173" r="51" fill="var(--white)"/>
    <circle cx="198" cy="173" r="47" fill="#8fb58a" role="img" aria-label="Photo of the modern white house with garden"/>
  </svg>
  <div class="abs brand" style="left:13px;top:14px;font-size:30px;color:var(--white)">Brisquelta</div>
  <div class="cover-title" style="left:31px;top:233px">BEAUTIFUL PRESENTATION</div>
  <div class="rule" style="left:22px;top:264px;width:261px"></div>
  <div class="cover-title" style="left:81px;top:273px">OF THE PROPERTIES</div>
  <div class="rule" style="left:80px;top:303px;width:203px"></div>
  <div class="for-sale">FOR SALE</div>
  <div class="abs brand brand-faint" style="left:8px;top:340px;font-size:44px;color:#f3f3f3">Brisquelta</div>
</section>

<!-- Location page -->
<section class="page p2">
  <div class="abs brand brand-faint" style="left:56px;top:18px">Brisquelta</div>
  <div class="frame" style="left:41px;top:64px;width:200px;height:141px">
    <div role="img" aria-label="Aerial map of the town on the lake shore" style="width:100%;height:100%;background:linear-gradient(200deg,#6f7f5e 0%,#5d6b57 45%,#2f6e7a 80%,#245f6c 100%)"></div>
  </div>
  <ul class="features">
    <li><b>Ihr neues Zuhause,</b> Rebhaldenweg 7, 8712 Stäfa</li>
    <li style="left:3px"><b>Bushaltestelle / S-Bahnhof</b></li>
    <li style="left:3px"><b>Einkaufsmöglichkeiten</b></li>
    <li style="left:3px"><b>Schule &amp; Kindergarten</b></li>
    <li style="left:3px"><b>Strandbadipsum</b></li>
  </ul>
  <div class="footer-url">www.brisquelta.com</div>
  <div class="footer-brand brand">Brisquelta</div>
  <div class="rule" style="left:22px;top:389px;width:261px"></div>
</section>

<!-- Municipality page -->
<section class="page p3">
  <svg class="shapes" width="283" height="396" viewBox="0 0 283 396">
    <polygon points="0,0 114,0 37,162 0,100" fill="var(--lime)"/>
    <polygon points="0,0 58,0 0,92" fill="var(--green)"/>
    <circle cx="104" cy="60" r="35" fill="var(--white)"/>
    <circle cx="104" cy="60" r="32" fill="#7ea37f" role="img" aria-label="Photo of the village church"/>
    <circle cx="64" cy="127" r="30" fill="var(--white)"/>
    <circle cx="64" cy="127" r="27" fill="#8aa4b4" role="img" aria-label="Photo of the lakeside harbour"/>
  </svg>
  <div class="abs brand brand-faint" style="left:153px;top:48px;font-size:19px">Brisquelta</div>
  <div class="frame" style="left:150px;top:75px;width:111px;height:76px;padding:2px">
    <div role="img" aria-label="Photo of the lakeside houses" style="width:100%;height:100%;background:linear-gradient(180deg,#3d5a78 0%,#9aa6a6 50%,#3e6d86 100%)"></div>
  </div>
  <div class="section-title" style="left:26px;top:166px;font-size:9px">DATEN UND FAKTEN ZUR GEMEINDE</div>
  <div class="abs body-copy" style="left:26px;top:182px;width:233px">
    <p>Stäfa – Unverwechselbar, sympathisch, echt – mit diesen Adjektiven wirbt die Zürichsee-Gemeinde Stäfa für ihre Qualitäten. Trotz ihrer Nähe zu Rapperswil und Zürich hat sie sich ihre Eigenständigkeit bewahrt und sich als eine der beliebtesten Wohngemeinden am See etabliert.</p>
    <p>Die sonnenverwöhnte Lage, die guten Verkehrsanbindungen sowie die kulturelle Vielfalt sprechen für sich. Geniessen Sie die Sommermonate in der Badi bzw. am schönen Ufer des Zürichsees, stöbern Sie in den reizenden Spezialitätengeschäften und geniessen Sie ein Abendessen in einem der vielen Restaurants.</p>
    <p>Stäfa bietet eine Vielzahl attraktiver Wander- und Walkingrouten, es gibt diverse Reitställe, einen Fussballverein, einen Tennisclub, einen Segelclub und vieles mehr.</p>
    <p>Die sonnenverwöhnten Hänge werden seit Generationen für traditionelle Weinsorten kultiviert, der Zürichsee als Wärmespeicher und die häufigen Föhnlagen bilden ideale Voraussetzungen und machen die Gemeinde Stäfa zur grössten Rebbaugemeinde des Kantons Zürich. 1969 wurden die Rebberge Kirchbühl, Lattenberg und Sternhalde sowie Risi Uerikon durch die Gemeindeversammlung vor der Überbauung bewahrt und unter Schutz gestellt.</p>
  </div>
  <div class="footer-url">www.brisquelta.com</div>
  <div class="footer-brand brand">Brisquelta</div>
  <div class="rule" style="left:22px;top:389px;width:261px"></div>
</section>

<!-- Short description -->
<section class="page p4">
  <div class="section-title" style="left:0;width:283px;text-align:center;top:40px;font-size:11.5px">KURZBESCHREIBUNG DES ANGEBOTES</div>
  <div class="rule center" style="left:32px;top:63px;width:219px"></div>
  <div class="label" style="left:46px;top:91px">Lagebeschreibung</div>
  <div class="col-text" style="top:92px">
    <p>Das geschmackvolle, einseitig angebaute 5½-Zimmer Einfamilienhaus wirkt äusserst modern und grosszügig, ohne dabei auf eine angenehme Leichtigkeit verzichten zu müssen.</p>
    <p>Leicht oberhalb des Zentrums, nahe unzähligen Wäldern, Feldern und Rebbergen, befindet sich Ihr neues Zuhause. Trotz der erhöhten Lage, erreichen Sie das Zentrum mit diversen Einkaufsmöglichkeiten, Bahnhof, Schulen und Kindergarten innert 10 Gehminuten. Bequemer geht es mit dem Bus (eine Gehminute entfernt).</p>
    <p>Dieser bietet direkten Anschluss an die S7 und neu auch an die S20 an. Die Stadt Zürich wie auch Rapperswil sind bestens mittels ÖV oder dem Auto erreichbar.</p>
  </div>
  <div class="label" style="left:46px;top:221px">Objektbeschreibung</div>
  <div class="col-text" style="top:222px">
    <p>Der moderne und doch dezent gehaltene Innenausbau weiss mit hochwertigen Materialien und einem durchdachten Raumkonzept zu überzeugen.</p>
    <p>Die Schlaf- und Wohnräume verteilen sich über drei Etagen, zuzüglich dem überaus grosszügigen Untergeschoss. Lichtkonzepte im und ums Haus, lichtdurchflutete Räume dank bodentiefen Fensterfronten, eine offene Küche mit angrenzendem Wohnbereich, moderne Nassräume, grosszügige Kinderzimmer, ein Elternschlafzimmer mit Ankleideraum und eigenem Badezimmer, eine Sauna und vieles mehr sorgen für ein Wohngefühl und Lebensstil auf hochstem Niveau.</p>
    <p>Umgeben wird dieses Schmuckstück von einem pflegeleichten, ganztägig besonnten Garten mit lauschigen Sitzplätzen, Spielmöglichkeit für Kinder, einem Kräutergarten und einer Panorama-Dachterrasse.</p>
  </div>
  <div class="footer-url">www.brisquelta.com</div>
  <div class="footer-brand brand">Brisquelta</div>
  <div class="rule" style="left:22px;top:389px;width:261px"></div>
</section>

<!-- Floor plan and conditions -->
<section class="page p5">
  <div class="section-title" style="left:0;width:283px;text-align:center;top:43px;font-size:11.5px">GRUNDRISS ZWEITES OBERGESCHOSS</div>
  <div class="rule center" style="left:32px;top:64px;width:219px"></div>
  <div class="abs" role="img" aria-label="Floor plan of the second upper floor with sauna, bath, room and roof terrace" style="left:35px;top:78px;width:89px;height:162px;background:linear-gradient(180deg,#dcdcdc 0%,#e4e4e4 60%,#eeeeee 100%)"></div>
  <div class="hyp-title">Die Hypothek</div>
  <div class="hyp-text">
    <p>Das Angebot wurde durch KELLMANN &amp; ROTH bewertet und für gut befunden.</p>
    <p>Der Kaufpreis in der Höhe von Total CHF 2'280'000.- (inkl. zwei Tiefgaragenplätze) wurde durch verschiedene Banken geprüft. Bitte beachten Sie die verschiedenen Empfehlungsschreiben im Anhang.</p>
  </div>
  <div class="cond-title">Konditionen</div>
  <div class="cond-row" style="top:280px"><span class="key">Übergabedatum</span><span class="val">Die Übergabe findet nach Vereinbarung statt.</span></div>
  <div class="cond-row" style="top:306px"><span class="key" style="top:6px">Verkaufspreis</span><span class="val">Der Verkaufspreis beträgt Total CHF 2'280'000.- inkl. zwei Tiefgaragenplätze.</span></div>
  <div class="cond-row" style="top:338px"><span class="key">Kosten</span><span class="val">Notariats- und Grundbuchgebühren gehen je zur Hälfte zu Lasten der Verkäuferschaft und Käuferschaft.</span></div>
  <div class="footer-url">www.brisquelta.com</div>
  <div class="footer-brand brand">Brisquelta</div>
  <div class="rule" style="left:22px;top:389px;width:261px"></div>
</section>

<!-- Back cover -->
<section class="page p6">
  <svg class="shapes" width="283" height="396" viewBox="0 0 283 396">
    <defs>
      <linearGradient id="gardenTone" x1="0" y1="0" x2="0" y2="1">
        <stop offset="0" stop-color="#4fa53a"/><stop offset="1" stop-color="#3d8a2b"/>
      </linearGradient>
    </defs>
    <polygon points="0,0 283,0 283,82 109,286 0,202" fill="url(#gardenTone)" role="img" aria-label="Photo of the garden with a large tree in green tint"/>
    <polygon points="0,202 109,286 283,82 283,100 109,306 0,226" fill="var(--band)"/>
    <polygon points="283,100 283,125 109,330 100,300 109,306" fill="var(--lime)" opacity="0"/>
    <polygon points="0,290 95,290 95,396 0,396" fill="var(--lime)"/>
    <polygon points="240,30 283,0 283,82 240,132" fill="#7fc24b" opacity=".35"/>
    <circle cx="82" cy="334" r="42" fill="var(--white)"/>
    <circle cx="82" cy="334" r="37" fill="#a9bda6" role="img" aria-label="Photo of the white modern house"/>
  </svg>
  <div class="abs brand" style="left:118px;top:205px;font-size:29px;color:var(--lime);transform:rotate(-49deg);transform-origin:left center">Brisquelta</div>
  <div class="contact">
    <div class="name">LENA BAUMANN</div>
    <div class="role">Manager</div>
    <div class="line"><span class="dot"></span>111-222-333</div>
    <div class="line"><span class="dot"></span>info@brisquelta.com</div>
    <div class="line"><span class="dot"></span>Your address, your city, box 88900</div>
  </div>
</section>

</body>
</html>
```